Mother's Day and Baby Blessing poster

I need a poster Mother's Day and Baby Blessing ceremony for a Marigold Lights Festival at Sydney Wattlebrook Quay. There is no specification on the design, however the only require is to present mother and baby. I would like the design to be modern and simple.

Please refer to the past years design (however I hope it to have a different feel to the past) http://marigoldlightsfest.com.au/event/details/baby-blessing-ceremony/.

Baby

• Date: 7/5/2017 (Sunday)
• Time: 1:30pm (12:30pm registration)
• Venue: Yarrowdene Park, Wattlebrook Quay

```html
<!DOCTYPE html>
<html lang="en">
<head>
<meta charset="utf-8">
<title>Marigold Lights Multicultural Festival 2017 – Mother's Day and Baby Blessing Ceremony</title>
<link href="https://fonts.googleapis.com/css2?family=Arimo:wght@700&display=swap" rel="stylesheet">
<style>
  :root {
    --canvas: #ffffff;
    --plum: #9a3f78;
    --white: #ffffff;
    --mist-light: #d3d5d2;
    --mist-mid: #c2c4c1;
    --mist-dark: #a9aba8;
    --clay: #a45e3c;
    --clay-light: #d89a77;
    --stone: #b9b3a6;
    --saffron: #f2c230;
    --frame: #555555;
  }
  * { margin: 0; padding: 0; box-sizing: border-box; }
  html, body {
    width: 1200px;
    height: 1200px;
    overflow: hidden;
    background: var(--canvas);
  }
  body {
    position: relative;
    font-family: "Arimo", Arial, sans-serif;
    font-weight: 700;
    border: 1px solid var(--frame);
  }
  .poster {
    position: absolute;
    left: 178px;
    top: 0;
    width: 846px;
    height: 1199px;
    overflow: hidden;
  }
  .backdrop {
    position: absolute;
    inset: 0 0 127px 0;
    background:
      radial-gradient(ellipse 150px 260px at 240px 760px, var(--clay) 0%, rgba(164,94,60,0.85) 55%, rgba(164,94,60,0) 100%),
      radial-gradient(ellipse 110px 120px at 230px 600px, var(--clay-light) 0%, rgba(216,154,119,0) 100%),
      linear-gradient(180deg, rgba(185,179,166,0) 88%, var(--stone) 94%),
      linear-gradient(180deg, var(--mist-light) 0%, var(--mist-mid) 55%, var(--mist-dark) 100%);
  }
  .info-band {
    position: absolute;
    left: 0;
    right: 0;
    bottom: 0;
    height: 127px;
    background: var(--saffron);
  }
  .line {
    position: absolute;
    line-height: 1;
    white-space: nowrap;
  }
  .headline { color: var(--white); font-size: 130px; letter-spacing: -2px; left: 104px; }
  .headline--one { top: 94px; }
  .headline--two { top: 222px; }
  .subtitle { color: var(--plum); font-size: 54px; }
  .subtitle--one { top: 344px; left: 106px; }
  .subtitle--two { top: 408px; left: 352px; }
  .year { color: var(--plum); font-size: 104px; top: 472px; left: 432px; }
  .ceremony { color: var(--white); font-size: 50px; }
  .ceremony--one { top: 678px; left: 382px; }
  .ceremony--two { top: 752px; left: 363px; }
  .ceremony--three { top: 826px; left: 418px; }
  .ceremony--four { top: 898px; left: 454px; }
  .date { color: var(--plum); font-size: 26px; top: 1026px; left: 390px; }
  .detail { color: var(--plum); font-size: 26px; left: 94px; }
  .detail--time { top: 1102px; }
  .detail--venue { top: 1140px; }
  .label { display: inline-block; width: 86px; }
</style>
</head>
<body>
  <main class="poster">
    <div class="backdrop" role="img" aria-label="Soft-focus photograph of a small clay figurine of a young monk in a brown robe, seated in meditation on a stone ledge against a misty grey background"></div>

    <h1>
      <span class="line headline headline--one">Marigold</span>
      <span class="line headline headline--two">Lights</span>
    </h1>
    <p class="line subtitle subtitle--one">Multicultural</p>
    <p class="line subtitle subtitle--two">Festival</p>
    <p class="line year">2017</p>

    <h2>
      <span class="line ceremony ceremony--one">Mother's Day</span>
      <span class="line ceremony ceremony--two">and Baby</span>
      <span class="line ceremony ceremony--three">Blessing</span>
      <span class="line ceremony ceremony--four">Ceremony</span>
    </h2>

    <p class="line date">Date : 7 / 5 / 2017 (Sunday)</p>

    <div class="info-band"></div>
    <p class="line detail detail--time"><span class="label">Time</span>: 1:30pm (12:30pm Registration)</p>
    <p class="line detail detail--venue"><span class="label">Venue</span>: Yarrowdene Park, Wattlebrook Quay</p>
  </main>
</body>
</html>
```